Brookvale Landscape & Construction Website

I have created a detailed txt document and included it in the files upload that will provide all the project details because trying to list it in here is cumbersome. This is for a website only. I have my own team to handle the psd to html conversion. They have an existing website which I have added in the doc. I have also upload various logo files to be used.

Industry/Entity Type

Landscape and Construction

Number of Pages Required

1 page

```html
<!DOCTYPE html>
<html lang="en">
<head>
<meta charset="UTF-8">
<title>Brookvale Landscape & Construction</title>
<link href="https://fonts.googleapis.com/css2?family=Comfortaa:wght@500&family=Jost:wght@600;700&display=swap" rel="stylesheet">
<style>
  :root {
    --white: #ffffff;
    --ink: #111111;
    --nav-orange: #f59a22;
    --nav-red: #d8202a;
    --nav-text: #3a2a14;
    --dot-active: #f59a22;
    --dot-idle: rgba(255,255,255,0.45);
    --hero-shade: rgba(0,0,0,0.22);
    --foliage-dark: #2f4a26;
    --foliage: #5f7d3e;
    --bloom: #b77a82;
    --mulch: #6a3a22;
    --walkway: #b9b6ad;
    --brick: #cfc6b8;
    --asphalt: #2a2c30;
  }
  html, body {
    margin: 0;
    padding: 0;
    width: 1200px;
    height: 675px;
    overflow: hidden;
    background: var(--white);
  }
  .page {
    position: relative;
    width: 1200px;
    height: 675px;
    overflow: hidden;
    background: var(--white);
  }
  .brand {
    position: absolute;
    top: 44px;
    left: 0;
    width: 1200px;
    display: flex;
    justify-content: center;
    align-items: center;
    gap: 14px;
  }
  .brand-dot {
    width: 44px;
    height: 44px;
    border-radius: 50%;
    background: var(--nav-orange);
  }
  .brand-name {
    font-family: 'Jost', sans-serif;
    font-weight: 700;
    font-size: 32px;
    color: var(--ink);
    letter-spacing: 0.3px;
  }
  .hero {
    position: absolute;
    top: 154px;
    left: 0;
    width: 1200px;
    height: 521px;
    background:
      linear-gradient(var(--hero-shade), var(--hero-shade)),
      radial-gradient(ellipse 380px 260px at 1010px 420px, rgba(42,44,48,0.95), rgba(42,44,48,0) 70%),
      radial-gradient(ellipse 220px 320px at 1130px 160px, rgba(207,198,184,0.95), rgba(207,198,184,0) 75%),
      radial-gradient(ellipse 320px 200px at 560px 300px, rgba(185,182,173,0.95), rgba(185,182,173,0) 70%),
      radial-gradient(ellipse 300px 220px at 300px 400px, rgba(183,122,130,0.9), rgba(183,122,130,0) 70%),
      radial-gradient(ellipse 260px 160px at 880px 300px, rgba(106,58,34,0.7), rgba(106,58,34,0) 70%),
      radial-gradient(ellipse 420px 220px at 640px 120px, rgba(95,125,62,0.95), rgba(95,125,62,0) 72%),
      linear-gradient(180deg, var(--foliage-dark) 0%, var(--foliage) 45%, var(--mulch) 100%);
  }
  .main-nav {
    position: absolute;
    top: 134px;
    left: 124px;
    width: 952px;
    height: 44px;
    background: var(--nav-orange);
    display: flex;
    align-items: center;
    z-index: 2;
  }
  .main-nav a {
    font-family: 'Comfortaa', sans-serif;
    font-weight: 500;
    font-size: 13.5px;
    color: var(--nav-text);
    text-decoration: none;
    height: 44px;
    display: flex;
    align-items: center;
    justify-content: center;
  }
  .main-nav .nav-home {
    width: 92px;
    background: var(--nav-red);
    color: var(--white);
  }
  .main-nav .nav-rest {
    flex: 1;
    display: flex;
    justify-content: space-around;
  }
  .hero-title {
    position: absolute;
    top: 369px;
    left: 0;
    width: 1200px;
    text-align: center;
    font-family: 'Jost', sans-serif;
    font-weight: 700;
    font-size: 32px;
    line-height: 41px;
    color: var(--white);
    text-shadow: 0 1px 3px rgba(0,0,0,0.35);
    margin: 0;
    z-index: 2;
  }
  .slide-arrow {
    position: absolute;
    top: 405px;
    width: 20px;
    height: 20px;
    z-index: 2;
  }
  .slide-arrow.prev { left: 52px; }
  .slide-arrow.next { left: 1128px; }
  .slide-dots {
    position: absolute;
    top: 619px;
    left: 542px;
    display: flex;
    gap: 5px;
    z-index: 2;
  }
  .slide-dots span {
    width: 25px;
    height: 4px;
    border-radius: 2px;
    background: var(--dot-idle);
  }
  .slide-dots span.active { background: var(--dot-active); }
</style>
</head>
<body>
<div class="page">
  <header class="brand">
    <div class="brand-dot"></div>
    <div class="brand-name">Brookvale Landscape &amp; Construction</div>
  </header>

  <div class="hero" role="img" aria-label="Front yard garden with pink flowering sedum, green shrubs, red mulch beds and a curved concrete walkway leading to a brick home porch beside a dark driveway"></div>

  <nav class="main-nav">
    <a class="nav-home" href="#">Home</a>
    <div class="nav-rest">
      <a href="#">Landscape Services</a>
      <a href="#">Construction Services</a>
      <a href="#">Company</a>
      <a href="#">Contact</a>
      <a href="#">FAQs</a>
      <a href="#">Gallery</a>
    </div>
  </nav>

  <h1 class="hero-title">We Offer Over 18 Years Experience In<br>Construction &amp; Landscaping</h1>

  <svg class="slide-arrow prev" viewBox="0 0 20 20"><polyline points="13,3 6,10 13,17" fill="none" stroke="#fff" stroke-width="3"/></svg>
  <svg class="slide-arrow next" viewBox="0 0 20 20"><polyline points="7,3 14,10 7,17" fill="none" stroke="#fff" stroke-width="3"/></svg>

  <div class="slide-dots">
    <span class="active"></span><span></span><span></span><span></span>
  </div>
</div>
</body>
</html>
```